Flyer Design Project

We are a Human Resources and payroll company with a dedicated staffing and recruiting division. We need a really professional looking and creative flyer that breifly explains our offerings. This flyer will be given to other sales people that sell complementary services to what we offer. Those salespeople will to leave this flyer with prospective clients that want services that do not offer and we do.
Updates

I just uploades our logo in EPS!  Thank you!

Target Market(s)

Employers are our target market. Mostly healthcare but not exclusively.

Industry/Entity Type

It Company

Requirements
Must have
• Photos of people in a working environment would be good. All offering in attached files must be in the flyer as well as our logo.
Nice to have
• It would be nice to convey that we care about our clients and their employees.

```html
<!DOCTYPE html>
<html lang="en">
<head>
<meta charset="utf-8">
<title>Recruiting and Staffing Packages</title>
<link rel="stylesheet" href="https://fonts.googleapis.com/css2?family=Roboto+Condensed:wght@700&family=Montserrat:wght@300;400;500;700&display=swap">
<style>
  :root {
    --bg-blue: #1b4bb0;
    --bg-blue-deep: #1640a0;
    --orange: #f7941d;
    --orange-light: #ffb347;
    --white: #ffffff;
    --note: #e4ecff;
    --glow: rgba(170, 215, 255, 0.22);
  }
  * { margin: 0; padding: 0; box-sizing: border-box; }
  html, body { width: 846px; height: 1200px; overflow: hidden; }
  body {
    position: relative;
    background: radial-gradient(ellipse at 50% 40%, var(--bg-blue) 0%, var(--bg-blue-deep) 100%);
    font-family: "Montserrat", Arial, sans-serif;
    color: var(--white);
  }
  .light-band {
    position: absolute; left: -40px; top: 250px; width: 940px; height: 90px;
    background: linear-gradient(180deg, transparent 0%, var(--glow) 50%, transparent 100%);
    transform: rotate(6deg);
  }
  .team-photo {
    position: absolute; left: 636px; top: 45px; width: 184px; height: 250px;
    background: linear-gradient(135deg, #c9d8ea 0%, #8fa6c4 45%, #2d3b55 100%);
  }
  .title {
    position: absolute; left: 62px; top: 88px;
    font-family: "Roboto Condensed", Arial, sans-serif; font-weight: 700; font-size: 42px;
    color: var(--orange);
    background: linear-gradient(180deg, var(--orange-light), var(--orange));
    -webkit-background-clip: text; background-clip: text; -webkit-text-fill-color: transparent;
    filter: drop-shadow(2px 2px 1px rgba(0,0,0,0.55));
  }
  .package { position: absolute; left: 38px; line-height: 24px; font-size: 18.5px; white-space: nowrap; }
  .package-name { color: var(--orange); font-weight: 400; font-size: 22px; line-height: 28px; }
  .package-name strong { font-weight: 700; margin-right: 36px; }
  .package-list { list-style: none; }
  .package-list li::before {
    content: "\25B6"; font-size: 16px; margin: 0 3px 0 7px; position: relative; top: -1px;
  }
  .package-note { font-size: 17px; font-weight: 300; color: var(--note); line-height: 21px; margin-top: 1px; }
  .package-d { font-size: 18.8px; }
  .package-intro .tight { font-size: 17.4px; }
</style>
</head>
<body>
  <div class="light-band" role="img" aria-label="Soft band of coloured light sweeping across the page"></div>
  <div class="team-photo" role="img" aria-label="Photo of a smiling businesswoman holding folders, with colleagues talking in an office behind her"></div>

  <h1 class="title">Recruiting and Staffing Packages</h1>

  <section class="package" style="top:282px">
    <h2 class="package-name"><strong>Package A</strong>$275.00</h2>
    <ul class="package-list">
      <li>Source up to 6 resumes</li>
      <li>Position is advertised on 1 job board</li>
    </ul>
    <p class="package-note">Note: Job Description is provided by client.&nbsp; We can provide<br>this service to you for an additional fee of $35)</p>
  </section>

  <section class="package" style="top:426px">
    <h2 class="package-name"><strong>Package B</strong>$ 390.00</h2>
    <ul class="package-list">
      <li>Source up to 8 resumes</li>
      <li>Position advertised on 2 job boards</li>
      <li>Phone screen prospective candidates utilizing position specific requirements<br>and questions provided by Client</li>
      <li>Client will be presented &nbsp;with a summarization of phone<br>screen along with prospective candidates resume</li>
    </ul>
    <p class="package-note">Note: Job Description is provided by client.&nbsp; We can provide this<br>service to you for an additional fee of $35)</p>
  </section>

  <section class="package" style="top:661px">
    <h2 class="package-name"><strong>Package C</strong>$ 625.00</h2>
    <ul class="package-list">
      <li>Source up to 10 resumes</li>
      <li>Create a customized job description that best fits your organizations needs</li>
      <li>Position advertised on 3 job boards</li>
      <li>Phone screen prospective candidates and conduct up to 3 in-person interviews<br>based on position specific requirements</li>
      <li>Client will be presented with a summarization of the interviews, based on a<br>candidate ranking system, as well as the prospective candidates resume.</li>
    </ul>
  </section>

  <section class="package package-d" style="top:900px">
    <h2 class="package-name"><strong>Package D</strong>Percentage of Prospective Candidates Annual Salary</h2>
    <p class="package-intro">Recruiter will take the time to learn about your organization so they can identify<br>individuals with qualities that will best match with your team. They will source,<br><span class="tight">conduct in-depth interviews via phone and in-person, as well as perform thorough</span><br>background and reference checks prior to employment.<br>Package also included:</p>
    <ul class="package-list">
      <li>Create a customized job description that best fits your organizations needs</li>
      <li>Position advertised on 3 job boards</li>
      <li>Client will be presented with a summarization of the interviews, based on a<br>candidate ranking system, as well as the prospective candidates resume.</li>
    </ul>
  </section>
</body>
</html>
```